Storefront signage for Physio clinic

We need a design for our storefront windows at our physiotherapy & Pilates clinic.

The design should be modern and include our logo, website url and services (physiotherapy, pilates, massage).

Some inspirational exercise/pilates/recovery quotes may be included and I would like to see the use of sport/pilates/injury related stock images. I have attached a few examples of what we want (images numbered 1-5). And I have attached our current design and photo of the outside of our clinic.

In the attached images there is also a pdf with measurments of our window panels. We require signage for the areas marked 1-10. As you can see on our current signage, you don't need to have a separate image for each panel, these can flow onto each other.

Industry/Entity Type

Clinic

Colors
85acd3
3377b5
3277b5
e8e8e8
c3c3c3
9d9d9d
848484
7f7f7f

Requirements
Must have
• Stock images related to sports, physiotherapy and pilates
• Ideally these images should be in greyscale and blend in with the rest of the panel which should include colours.
• I would like to see for example a runner, a weightlifter, someone doing pilates, someone with back pain (not necessarily all of these).
Should not have
• I want a creative, modern, up market design, not just a standard recycled template.

```html
<!DOCTYPE html>
<html lang="en">
<head>
<meta charset="utf-8">
<title>Northbank Physio &amp; Pilates – Window Signage</title>
<link rel="stylesheet" href="https://fonts.googleapis.com/css2?family=Montserrat:ital,wght@0,400;0,600;0,800;1,400&display=swap">
<style>
  :root {
    --blue-light: #85acd3;
    --blue: #3377b5;
    --blue-deep: #1f4f9c;
    --navy: #1b3e86;
    --grey-pale: #e8e8e8;
    --grey-light: #c3c3c3;
    --grey-mid: #9d9d9d;
    --grey-dark: #848484;
    --grey-shadow: #3a3a3a;
    --ink: #2b2b2b;
    --white: #ffffff;
    --backdrop: #f2f2f2;
  }
  * { box-sizing: border-box; margin: 0; padding: 0; }
  html, body { width: 1200px; height: 591px; overflow: hidden; }
  body { background: var(--backdrop); font-family: "Montserrat", sans-serif; position: relative; }

  .panel { position: absolute; overflow: hidden; }
  .panel__band {
    position: absolute; top: 0; left: 0; right: 0; height: 12px;
    background: linear-gradient(90deg, var(--blue-light) 0 45%, var(--blue) 45% 100%);
    z-index: 2;
  }
  .panel__photo { position: absolute; inset: 12px 0 0 0; }

  .brand { position: absolute; display: flex; align-items: center; gap: 4px; white-space: nowrap; }
  .brand__dot { width: 9px; height: 9px; border-radius: 50%; background: var(--blue); flex: none; }
  .brand__name { font-weight: 800; font-size: 9px; color: var(--blue); letter-spacing: .5px; }

  /* Window 1 – weightlifter */
  .window-sweat { left: 10px; top: 153px; width: 334px; height: 267px; }
  .window-sweat .panel__photo {
    background:
      radial-gradient(ellipse 90px 70px at 70px 40px, rgba(40,40,40,.85), transparent 70%),
      radial-gradient(ellipse 120px 90px at 150px 200px, rgba(30,30,30,.9), transparent 70%),
      radial-gradient(ellipse 110px 40px at 110px 30px, rgba(235,235,235,.7), transparent 70%),
      radial-gradient(ellipse 90px 120px at 280px 110px, rgba(220,220,220,.55), transparent 70%),
      radial-gradient(ellipse 70px 50px at 210px 230px, rgba(240,240,240,.6), transparent 70%),
      linear-gradient(100deg, #2e2e2e 0%, #5a5a5a 35%, var(--grey-dark) 60%, var(--grey-light) 100%);
  }
  .window-sweat .brand { right: 20px; top: 46px; }
  .window-sweat .brand__name { color: var(--white); }
  .window-sweat .brand__dot { background: var(--white); }
  .headline-sweat { position: absolute; left: 80px; top: 112px; font-weight: 800; font-size: 29px; line-height: 1; color: var(--blue-light); }
  .headline-sweat__tag { display: block; font-weight: 600; font-size: 10px; color: var(--white); margin-top: 6px; }
  .services-box { position: absolute; left: 242px; top: 123px; width: 86px; height: 63px; background: var(--navy); padding: 7px 6px; list-style: none; }
  .services-box li { font-size: 5.5px; font-weight: 600; color: var(--white); letter-spacing: .3px; margin-bottom: 8px; white-space: nowrap; }
  .services-box li:last-child { margin-bottom: 0; }
  .enrol { position: absolute; left: 242px; top: 210px; width: 86px; height: 12px; background: var(--navy); color: var(--white); font-size: 6px; font-weight: 800; text-align: center; line-height: 12px; }
  .web-sweat { position: absolute; right: 8px; bottom: 14px; font-size: 6px; color: var(--white); }

  /* Window 2 – Pilates on balls */
  .window-restore { left: 411px; top: 159px; width: 338px; height: 267px; }
  .window-restore .panel__photo {
    background:
      radial-gradient(ellipse 60px 80px at 130px 70px, rgba(90,90,90,.55), transparent 70%),
      radial-gradient(ellipse 110px 40px at 150px 180px, rgba(70,70,70,.5), transparent 70%),
      radial-gradient(ellipse 60px 60px at 260px 115px, rgba(60,60,60,.6), transparent 70%),
      radial-gradient(circle 55px at 290px 190px, rgba(250,250,250,.85), transparent 75%),
      radial-gradient(circle 40px at 95px 40px, rgba(200,200,200,.7), transparent 75%),
      linear-gradient(120deg, var(--grey-pale) 0%, var(--grey-light) 45%, var(--grey-mid) 70%, var(--grey-pale) 100%);
  }
  .window-restore .brand { right: 16px; top: 48px; }
  .headline-restore { position: absolute; left: 30px; top: 132px; font-weight: 800; font-size: 20px; line-height: 1.05; color: var(--blue-deep); }
  .headline-restore__tag { display: block; font-weight: 400; font-style: italic; font-size: 10px; color: var(--ink); margin: 3px 0 0 80px; }
  .web-restore { position: absolute; left: 30px; bottom: 28px; font-size: 6px; color: var(--ink); }

  /* Door side panels */
  .door-panel { top: 167px; height: 270px; background: linear-gradient(180deg, var(--navy), var(--blue-deep)); }
  .door-panel--left { left: 813px; width: 108px; }
  .door-panel--right { left: 1074px; width: 115px; }
  .door-panel .panel__band { height: 10px; background: var(--blue); }
  .service { position: absolute; left: 0; right: 0; text-align: center; }
  .service__photo { width: 42px; height: 42px; border-radius: 50%; margin: 0 auto; background: radial-gradient(circle at 40% 35%, var(--grey-pale), var(--grey-mid) 70%, var(--grey-dark)); border: 2px solid var(--white); }
  .service__label { display: block; margin-top: 5px; font-size: 5px; font-weight: 600; color: var(--white); letter-spacing: .4px; white-space: nowrap; }
  .phone { position: absolute; left: 0; right: 0; bottom: 12px; text-align: center; font-size: 6.5px; font-weight: 600; color: var(--white); }
  .address { position: absolute; left: 14px; bottom: 10px; font-size: 5px; line-height: 1.5; color: var(--white); }

  /* Entry door glass */
  .door-glass { left: 921px; top: 167px; width: 153px; height: 270px; background: linear-gradient(180deg, #dfe6ec, #eef1f3); }
  .door-glass__split { position: absolute; left: 76px; top: 0; bottom: 0; width: 1px; background: var(--grey-light); }
  .door-emblem { position: absolute; left: 17px; top: 89px; width: 118px; height: 118px; border-radius: 50%; border: 2px solid var(--blue-light); display: flex; align-items: center; justify-content: center; }
  .door-emblem .brand__name { font-size: 11px; color: var(--blue); }
</style>
</head>
<body>

  <section class="panel window-sweat">
    <div class="panel__band"></div>
    <div class="panel__photo" role="img" aria-label="Greyscale photo of a weightlifter gripping a barbell"></div>
    <div class="brand"><span class="brand__dot"></span><span class="brand__name">NORTHBANK</span></div>
    <h2 class="headline-sweat">GOOD<br>THINGS<span class="headline-sweat__tag">come to those who sweat</span></h2>
    <ul class="services-box">
      <li>PHYSIOTHERAPY</li><li>PILATES</li><li>MASSAGE</li><li>WORK REHABILITATION</li>
    </ul>
    <div class="enrol">ENROL NOW!</div>
    <p class="web-sweat">www.northbankphysio.example</p>
  </section>

  <section class="panel window-restore">
    <div class="panel__band"></div>
    <div class="panel__photo" role="img" aria-label="Greyscale photo of women doing Pilates on exercise balls"></div>
    <div class="brand"><span class="brand__dot"></span><span class="brand__name">NORTHBANK</span></div>
    <h2 class="headline-restore">BODY<br>RESTORATION<span class="headline-restore__tag">the natural way...</span></h2>
    <p class="web-restore">www.northbankphysio.example</p>
  </section>

  <section class="panel door-panel door-panel--left">
    <div class="panel__band"></div>
    <div class="service" style="top:88px"><div class="service__photo" role="img" aria-label="Physiotherapy treatment photo"></div><span class="service__label">PHYSIOTHERAPY</span></div>
    <div class="service" style="top:150px"><div class="service__photo" role="img" aria-label="Pilates class photo"></div><span class="service__label">PILATES</span></div>
    <p class="phone">02 5550 1234</p>
  </section>

  <section class="panel door-glass">
    <div class="door-glass__split"></div>
    <div class="door-emblem"><span class="brand__name">NORTHBANK</span></div>
  </section>

  <section class="panel door-panel door-panel--right">
    <div class="panel__band"></div>
    <div class="service" style="top:88px"><div class="service__photo" role="img" aria-label="Massage therapy photo"></div><span class="service__label">MASSAGE</span></div>
    <div class="service" style="top:150px"><div class="service__photo" role="img" aria-label="Work rehabilitation exercise photo"></div><span class="service__label">WORK REHABILITATION</span></div>
    <p class="address">Shop 4, 12 Harbour St<br>Northbank<br>www.northbankphysio.example</p>
  </section>

</body>
</html>
```